Seeking funky, innovative business cards

I am looking to refresh our current business cards to something more engaging, visual and impactful. We are a management consultancy firm, see website (www.larkspur-advisory.com.au). I've included our colour scheme, sample of the slides we use and our old business cards. We would like our cards to have icons. The card should display:- Name- Title- Mobile number- Address- Email address- Website - Company logo- Our purpose statement "We create the best places on earth to work"

Contact Information for Business Card

Tavish Brellan
Consultant
0491 672 348
Level 5, 218 Warrick Lane, Melbourne 3000
tavish@larkspur-advisory.com.au
www.larkspur-advisory.com.au

Purpose statement "we create the best places on earth to work"
LOGO available in google images

Font styles to use
Other font styles liked:
• Open Sans Light, Bebas Neue (open to other cool foints)

Colors
ffc214
5c5c5c
f5f5f5
fefefe

Requirements
Must have
• - Name
• - Title
• - Mobile number
• - Address
• - Email address
• - Website
• - Company logo
• - Our purpose statement "We create the best places on earth to work"
Nice to have
• - Icons
• - Colour (see our colour scheme"

```html
<!DOCTYPE html>
<html lang="en">
<head>
<meta charset="utf-8">
<title>Tavish Brellan – Business Card</title>
<link rel="stylesheet" href="https://fonts.googleapis.com/css2?family=Bebas+Neue&family=Open+Sans:wght@300;400&display=swap">
<style>
  :root {
    --ink: #454b4b;
    --accent: #f7a535;
    --band-start: #ffd400;
    --band-end: #f9a535;
    --paper: #ffffff;
  }
  html, body {
    margin: 0;
    padding: 0;
    overflow: hidden;
    background: var(--paper);
  }
  .card {
    position: relative;
    width: 1200px;
    height: 720px;
    background: var(--paper);
    overflow: hidden;
  }
  .brand {
    position: absolute;
    left: 122px;
    top: 72px;
    display: flex;
    align-items: center;
    gap: 14px;
  }
  .brand__mark {
    width: 30px;
    height: 30px;
    border-radius: 50%;
    background: var(--accent);
  }
  .brand__name {
    font-family: "Bebas Neue", "Oswald", sans-serif;
    font-size: 40px;
    line-height: 1;
    letter-spacing: 1px;
    color: var(--ink);
    padding-top: 4px;
  }
  .identity__name {
    position: absolute;
    right: 633px;
    top: 302px;
    margin: 0;
    font-family: "Bebas Neue", "Oswald", sans-serif;
    font-weight: 400;
    font-size: 88px;
    line-height: 1;
    letter-spacing: 1px;
    color: var(--ink);
    white-space: nowrap;
  }
  .identity__title {
    position: absolute;
    right: 631px;
    top: 386px;
    margin: 0;
    font-family: "Open Sans", sans-serif;
    font-weight: 300;
    font-size: 26px;
    line-height: 1;
    color: var(--accent);
  }
  .divider {
    position: absolute;
    left: 597px;
    top: 291px;
    width: 3px;
    height: 141px;
    background: var(--ink);
  }
  .contacts {
    position: absolute;
    left: 625px;
    top: 283px;
    margin: 0;
    padding: 0;
    list-style: none;
  }
  .contacts__item {
    display: flex;
    align-items: center;
    height: 38px;
    font-family: "Open Sans", sans-serif;
    font-weight: 300;
    font-size: 25px;
    letter-spacing: 0.6px;
    color: var(--ink);
    white-space: nowrap;
  }
  .contacts__icon {
    width: 30px;
    height: 30px;
    margin-right: 16px;
    flex: none;
  }
  .contacts__domain { color: var(--accent); }
  .band {
    position: absolute;
    left: 0;
    bottom: 0;
    box-sizing: border-box;
    width: 1200px;
    height: 49px;
    padding: 0 60px 0 122px;
    display: flex;
    align-items: center;
    justify-content: space-between;
    background: linear-gradient(90deg, var(--band-start), var(--band-end));
    font-family: "Open Sans", sans-serif;
    font-weight: 400;
    font-size: 18px;
    color: var(--ink);
    white-space: nowrap;
  }
  .band__purpose { margin: 0; letter-spacing: 0.4px; }
  .band__address {
    margin: 0;
    display: flex;
    align-items: center;
    gap: 8px;
    font-style: normal;
  }
  .band__pin { width: 16px; height: 20px; flex: none; }
</style>
</head>
<body>
  <main class="card">
    <div class="brand">
      <span class="brand__mark"></span>
      <span class="brand__name">Larkspur Advisory</span>
    </div>

    <h1 class="identity__name">Tavish Brellan</h1>
    <p class="identity__title">Consultant</p>
    <div class="divider"></div>

    <ul class="contacts">
      <li class="contacts__item">
        <svg class="contacts__icon" viewBox="0 0 30 30" aria-hidden="true">
          <circle cx="15" cy="15" r="14" fill="var(--accent)"/>
          <rect x="10.5" y="7" width="9" height="16" rx="1.5" fill="none" stroke="var(--ink)" stroke-width="2"/>
          <circle cx="15" cy="20" r="1" fill="var(--ink)"/>
        </svg>
        0491 672 348
      </li>
      <li class="contacts__item">
        <svg class="contacts__icon" viewBox="0 0 30 30" aria-hidden="true">
          <circle cx="15" cy="15" r="14" fill="var(--accent)"/>
          <rect x="6.5" y="11.5" width="10" height="7" rx="3.5" fill="none" stroke="var(--ink)" stroke-width="2"/>
          <rect x="13.5" y="11.5" width="10" height="7" rx="3.5" fill="none" stroke="var(--ink)" stroke-width="2"/>
        </svg>
        www.connectwork.net/in/tavishb/
      </li>
      <li class="contacts__item">
        <svg class="contacts__icon" viewBox="0 0 30 30" aria-hidden="true">
          <circle cx="15" cy="15" r="14" fill="var(--accent)"/>
          <rect x="7.5" y="10" width="15" height="11" rx="1" fill="none" stroke="var(--ink)" stroke-width="2"/>
          <polyline points="8,11 15,16.5 22,11" fill="none" stroke="var(--ink)" stroke-width="2"/>
        </svg>
        tavish@<span class="contacts__domain">larkspur-advisory</span>.com.au
      </li>
      <li class="contacts__item">
        <svg class="contacts__icon" viewBox="0 0 30 30" aria-hidden="true">
          <circle cx="15" cy="15" r="14" fill="var(--accent)"/>
          <circle cx="16.5" cy="13.5" r="5.5" fill="none" stroke="var(--ink)" stroke-width="2.2"/>
          <line x1="12.5" y1="17.5" x2="8" y2="22" stroke="var(--ink)" stroke-width="2.6" stroke-linecap="round"/>
        </svg>
        www.<span class="contacts__domain">larkspur-advisory</span>.com.au
      </li>
    </ul>

    <footer class="band">
      <p class="band__purpose">We create the best places on earth to work</p>
      <address class="band__address">
        <svg class="band__pin" viewBox="0 0 16 20" aria-hidden="true">
          <path d="M8 1a6 6 0 0 0-6 6c0 4.5 6 12 6 12s6-7.5 6-12a6 6 0 0 0-6-6z" fill="none" stroke="var(--ink)" stroke-width="1.8"/>
          <circle cx="8" cy="7" r="2.2" fill="var(--ink)"/>
        </svg>
        Level 5, 218 Warrick Lane, Melbourne 3000
      </address>
    </footer>
  </main>
</body>
</html>
```